Corvane: The Quiet Lantern

I need a front, back and spine cover for e and print for a short book. The book is called Corvane, subtitle, The Quiet Lantern. It is about an eyewitness to the Archangel Corvane. I would like to use the design many times with different colours for a series in spirituality and magic. So hopefully I can work with the designer again. The simple idea, is a plain cover in a colour, here blue. Mostly a font based cover, with a small symbolic image silhouetted at the bottom. Other covers will be orange, same font, and a different silhouette symbolic image and so on.

We need: a blue that will print well and look good on a screen. Serious, inviting honesty and truth and not flat. A font that is modern, female, says mystic but not old saint. The author is female and an award-winning writer in different areas. We need a uniform space for a title, (here Corvane), a uniform space for "The Quiet Lantern", a small space for a simple symbolic image, and author name, Wren Halloway. The small image on this blue cover should be in red. Ideas would be a simple rose head. The cover must look modern and professional and compliment the brand at www.wrenhalloway-books.com.

If the designer would simultaneously like to pitch to design the whole series (which will have many titles), another one would be a warm/hot pink background with the title Blue Harbour, subtitle, Brighten Every Ordinary Week. Small image silhouetted in orange might be a small gift shape, or a seahorse. Same author name, Wren Halloway. Another cover would be green background, title Lanterns: subtitle, Seven Rivers Beyond the Hill. Image in yellow: a rolled yoga mat, or an Om symbol. Wren Halloway. If we find a groove for the whole series, I can keep working with the same designer. Of course, the cover just for Corvane is fine here, but please bear in mind it fits into this wider series. Blue covers are about conversation with or contact with key spiritual figures, each from the author's own personal experience. Another one there would be "Swami Dhorelan", Letters From a Northern Garden. Image would be a simple daisy or a trophy emblem in red.

Font is crucial here and will define a series. Modern spirituality for the current generation. It must suggest contact with higher planes without being chintzy. Thank you!

Simple designs are iconic. That is what we are going for!

Good luck.

Target Market(s)

The people who read iconic series books like old marlow classics

Colors
34a6d7

Requirements
Must have
• modern, iconic, translatable into different markets.
Nice to have
• symbolic images silhouetted into a colour, not black, as the guidelines.
Should not have
• not too emotional.

```html
<!DOCTYPE html>
<html lang="en">
<head>
<meta charset="utf-8">
<title>Corvane: The Quiet Lantern — Wren Halloway</title>
<link rel="stylesheet" href="https://fonts.googleapis.com/css2?family=Caveat+Brush&family=Open+Sans:wght@400&display=swap">
<style>
  :root {
    --cover-blue: #4f8fbd;
    --cover-blue-deep: #2f6a99;
    --cover-blue-edge: #1d4c75;
    --cover-blue-mist: #a9cde4;
    --cover-blue-glow: #e4f0f7;
    --type-white: #ffffff;
    --emblem-red: #d7191f;
    --emblem-red-dark: #a10f14;
    --emblem-leaf: #4a7a2c;
  }
  html, body {
    margin: 0;
    padding: 0;
    width: 800px;
    height: 1200px;
    overflow: hidden;
    background: var(--cover-blue-edge);
  }
  .book-cover {
    position: relative;
    width: 800px;
    height: 1200px;
    overflow: hidden;
    background:
      radial-gradient(ellipse 380px 460px at 400px 800px, var(--cover-blue-glow) 0%, rgba(228,240,247,0.7) 35%, rgba(169,205,228,0) 80%),
      radial-gradient(ellipse 620px 820px at 400px 700px, var(--cover-blue-mist) 0%, var(--cover-blue) 55%, var(--cover-blue-deep) 80%, var(--cover-blue-edge) 100%);
  }
  .cover-title {
    position: absolute;
    top: 95px;
    left: 0;
    width: 800px;
    margin: 0;
    text-align: center;
    font-family: "Caveat Brush", cursive;
    font-weight: 400;
    font-size: 236px;
    line-height: 1;
    letter-spacing: 0;
    color: var(--type-white);
  }
  .cover-subtitle {
    position: absolute;
    top: 418px;
    left: 0;
    width: 800px;
    margin: 0;
    text-align: center;
    font-family: "Caveat Brush", cursive;
    font-weight: 400;
    font-size: 76px;
    line-height: 1.2;
    color: var(--type-white);
  }
  .cover-emblem {
    position: absolute;
    left: 240px;
    top: 664px;
    width: 345px;
    height: 278px;
  }
  .cover-author {
    position: absolute;
    top: 1028px;
    left: 0;
    width: 800px;
    margin: 0;
    text-align: center;
    font-family: "Open Sans", sans-serif;
    font-weight: 400;
    font-size: 62px;
    line-height: 1.2;
    color: var(--type-white);
  }
</style>
</head>
<body>
  <main class="book-cover">
    <h1 class="cover-title">Corvane</h1>
    <p class="cover-subtitle">The Quiet Lantern</p>
    <svg class="cover-emblem" viewBox="0 0 345 278" role="img" aria-label="A single red rose head with green leaves, the book's symbolic emblem">
      <defs>
        <radialGradient id="emblem-tone" cx="46%" cy="32%" r="70%">
          <stop offset="0%" stop-color="var(--emblem-red-dark)"/>
          <stop offset="45%" stop-color="var(--emblem-red)"/>
          <stop offset="75%" stop-color="var(--emblem-red)" stop-opacity="0.85"/>
          <stop offset="100%" stop-color="var(--emblem-leaf)" stop-opacity="0.55"/>
        </radialGradient>
      </defs>
      <ellipse cx="165" cy="120" rx="150" ry="112" fill="url(#emblem-tone)"/>
    </svg>
    <p class="cover-author">Wren Halloway</p>
  </main>
</body>
</html>
```